Design my dad a new business card because his current one sucks!

I need a business card designed for my fathers home maintenance business. His customers are individuals (single moms, old people etc.) as well as the occasional business. As such it needs to be accessible to both target audiences.

The front of the card should be dark grey on yellow with the logo and contain the following information:
- Darren Whitlock
- 0488 372 915
- info@bluegumhomecare.example.au
- 0488 372 915

- ABN: 71 284 630 912
- 'Fully Insured'

The reverse should be yellow on dark grey and will have the web address:
- bluegumhomecare.example.au

And a few key services he offers:
GENERAL REPAIRS
PAINTING/TILING/
PAVING &CONCRETING
PRESSURE WASHING
ON-SITE WELDING
DECKING ADDITIONS & REPAIRS
FENCING
FULL BOND CLEANING

This will be first time the logo has been printed so you will need to come up with the best CMYK approximation of the RGB colours to make sure it is a close as possible.

```html
<!DOCTYPE html>
<html lang="en">
<head>
<meta charset="utf-8">
<title>Bluegum Home Care – Business Card</title>
<link href="https://fonts.googleapis.com/css2?family=Poppins:wght@400;600;700&display=swap" rel="stylesheet">
<style>
  :root {
    --yellow: #f0d000;
    --yellow-deep: #d4b400;
    --charcoal: #333335;
    --charcoal-soft: #3c3c3e;
    --backdrop: #1e1e1f;
    --font: "Poppins", "Century Gothic", sans-serif;
  }
  * { box-sizing: border-box; margin: 0; padding: 0; }
  html, body { width: 1200px; height: 900px; overflow: hidden; }
  body {
    background: var(--backdrop);
    font-family: var(--font);
    position: relative;
  }
  .card {
    position: absolute;
    left: 250px;
    width: 700px;
    height: 400px;
    overflow: hidden;
    border-radius: 3px;
  }
  .card--back { top: 35px; background: var(--charcoal); color: var(--yellow); }
  .card--front {
    top: 465px;
    background: radial-gradient(ellipse at 30% 30%, var(--yellow) 0%, var(--yellow-deep) 100%);
    color: var(--charcoal);
  }

  /* wordmark */
  .wordmark {
    position: absolute;
    display: flex;
    align-items: center;
    gap: 14px;
    font-weight: 700;
    letter-spacing: 1px;
    line-height: 1;
  }
  .wordmark__dot { width: 34px; height: 34px; border-radius: 50%; background: currentColor; }
  .wordmark__name { font-size: 40px; text-transform: uppercase; }

  /* back */
  .card--back .wordmark { left: 90px; top: 70px; }
  .services {
    position: absolute;
    left: 90px;
    top: 150px;
    width: 540px;
    list-style: none;
    font-size: 15px;
    font-weight: 400;
    letter-spacing: 1px;
    line-height: 1.75;
    text-transform: uppercase;
  }
  .services li { display: inline; }
  .services li + li::before { content: " • "; }
  .web-pill {
    position: absolute;
    left: 90px;
    bottom: 60px;
    padding: 8px 26px;
    border-radius: 22px;
    background: var(--yellow);
    color: var(--charcoal);
    font-size: 17px;
    letter-spacing: 0.5px;
  }

  /* front */
  .card--front .wordmark { left: 60px; top: 70px; }
  .contact { position: absolute; left: 60px; top: 210px; }
  .contact__name { font-size: 24px; font-weight: 600; }
  .contact__role { font-size: 16px; margin-bottom: 26px; }
  .contact__line { font-size: 17px; line-height: 1.5; letter-spacing: 0.3px; }
  .disc {
    position: absolute;
    left: 520px;
    top: 140px;
    width: 300px;
    height: 300px;
    border-radius: 50%;
    background: var(--charcoal-soft);
  }
  .credentials {
    position: absolute;
    left: 565px;
    top: 245px;
    color: var(--yellow);
    font-size: 13px;
    line-height: 1.5;
    letter-spacing: 0.5px;
    text-transform: uppercase;
    white-space: nowrap;
  }
</style>
</head>
<body>
  <section class="card card--back" aria-label="Card reverse">
    <div class="wordmark"><span class="wordmark__dot"></span><span class="wordmark__name">Bluegum Home Care</span></div>
    <ul class="services">
      <li>General repairs</li><li>Painting / tiling</li><li>Paving &amp; concreting</li><li>Pressure washing</li><li>On-site welding</li><li>Fencing</li><li>Decking additions &amp; repairs</li><li>Full bond cleaning</li>
    </ul>
    <div class="web-pill">bluegumhomecare.example.au</div>
  </section>

  <section class="card card--front" aria-label="Card front">
    <div class="wordmark"><span class="wordmark__dot"></span><span class="wordmark__name">Bluegum Home Care</span></div>
    <div class="contact">
      <p class="contact__name">Darren Whitlock</p>
      <p class="contact__role">owner</p>
      <p class="contact__line">0488 372 915</p>
      <p class="contact__line">info@bluegumhomecare.example.au</p>
      <p class="contact__line">bluegumhomecare.example.au</p>
    </div>
    <div class="disc"></div>
    <div class="credentials">
      <p>ABN: 71 284 630 912</p>
      <p>Fully insured</p>
    </div>
  </section>
</body>
</html>
```